Lost Teens Auto Doantion Website Design

Please create a new one page website design.

Current site: http://autosforyouth.net/

New WEBSITE address is: SedansForLostTeens.org

Use these sites for an idea of what I am looking for. I like these sites best: tiresforretirees.org and trucksforelders.org

Coding

Coded - Design and coding required

Number of Pages Required

1 page

```html
<!DOCTYPE html>
<html lang="en">
<head>
<meta charset="utf-8">
<title>Northbeam Rescue Fund</title>
<link href="https://fonts.googleapis.com/css2?family=Montserrat:ital,wght@0,400;0,500;0,600;0,700;1,500&display=swap" rel="stylesheet">
<style>
:root{
  --blue:#2e6bbf;
  --blue-dark:#1f3a5e;
  --teal-heading:#2a6a94;
  --ink:#333333;
  --muted:#666666;
  --light-bg:#f4f4f4;
  --band-grey:#3f3f3f;
  --band-grey-2:#474747;
  --stats-bg:#141414;
  --footer-bg:#282828;
  --white:#ffffff;
  --field-border:#cfcfcf;
}
*{margin:0;padding:0;box-sizing:border-box}
html,body{width:1200px;height:2778px;overflow:hidden}
body{font-family:"Montserrat",sans-serif;color:var(--ink);background:var(--white);position:relative}
.section{position:absolute;left:0;width:1200px}
.abs{position:absolute}

/* hero */
.hero{top:0;height:650px;background:linear-gradient(90deg,#152a33 0%,#1f3c46 45%,#3d5f68 70%,#1d3540 100%)}
.hero-photo{position:absolute;inset:0}
.logo{left:22px;top:32px;font-size:15px;font-weight:700;color:var(--white);letter-spacing:-.3px}
.nav{right:30px;top:28px;display:flex;align-items:center;gap:20px}
.nav a{color:var(--white);text-decoration:none;font-size:11px;font-weight:600;letter-spacing:1px}
.nav .nav-donate{border:2px solid var(--white);padding:7px 14px}
.hero-title{left:128px;top:236px;font-size:74px;font-weight:700;color:var(--white)}
.hero-tag{left:130px;top:331px;font-size:15px;font-style:italic;font-weight:500;color:var(--white)}
.btn{display:inline-flex;align-items:center;justify-content:center;font-size:10px;font-weight:600;letter-spacing:1.5px;color:var(--white);text-transform:uppercase}
.btn-fill{background:var(--blue)}
.btn-line{border:2px solid var(--white)}
.hero-donate{left:128px;top:394px;width:105px;height:30px}
.hero-more{left:257px;top:394px;width:141px;height:30px}

/* about */
.about{top:650px;height:235px;background:var(--light-bg);text-align:center}
.section-title{font-size:40px;font-weight:700;color:var(--ink)}
.rule{height:1px;width:370px;background:#d8d8d8;margin:0 auto}
.about .section-title{position:absolute;left:0;right:0;top:50px}
.about .rule{position:absolute;left:415px;top:109px}
.about p{position:absolute;left:133px;width:934px;top:138px;font-size:13.5px;line-height:19px;color:var(--muted)}
.about-band{top:885px;height:96px;background:var(--band-grey)}
.about-band .btn{position:absolute;left:550px;top:11px;width:98px;height:26px;background:var(--blue-dark);color:#5a7395;font-size:9px}

/* gallery */
.gallery{top:981px;height:226px;display:flex}
.gallery-tile{flex:1;height:100%}
.tile-1{background:linear-gradient(160deg,#2a2a2a,#4a4440)}
.tile-2{background:linear-gradient(160deg,#3a3632,#6b6156)}
.tile-3{background:linear-gradient(160deg,#544536,#8a7560)}
.tile-4{background:linear-gradient(160deg,#2e2b29,#564c44)}

.donate-band{top:1207px;height:145px;background:var(--band-grey-2);text-align:center}
.donate-band .section-title{position:absolute;left:0;right:0;top:44px;color:#222}
.donate-band .rule{position:absolute;left:470px;top:100px;width:260px;background:#5a5a5a}

/* form */
.contact{top:1352px;height:572px;background:#f5f5f5}
.pitch-title{left:130px;top:34px;font-size:41px;line-height:42px;font-weight:700;color:var(--teal-heading);width:420px}
.pitch-list{left:134px;top:128px;list-style:none;font-size:21px;line-height:30px;color:#444}
.pitch-list li::before{content:"•";margin-right:10px;font-size:16px}
.form{left:609px;top:28px;width:462px}
.field-label{display:block;font-size:13px;line-height:16px;color:#555;margin-bottom:5px}
.field{width:462px;height:41px;background:#f5f5f5;border:1px solid var(--field-border);margin-bottom:19px}
.field-area{height:193px;margin-bottom:26px}
.send{width:67px;height:36px;font-size:11px;letter-spacing:.5px;text-transform:none}

/* stats */
.stats{top:1924px;height:239px;background:var(--stats-bg)}
.stat{top:76px;width:300px;text-align:center;color:var(--white)}
.stat-num{font-size:48px;font-weight:500;color:var(--blue);line-height:48px}
.stat-label{font-size:13px;line-height:19px;margin-top:8px}

/* call to action */
.cta{top:2163px;height:404px;background:radial-gradient(ellipse at 55% 55%,#6e5a3e 0%,#3b3125 45%,#1e1b16 100%);text-align:center}
.cta-title{position:absolute;left:0;right:0;top:140px;font-size:40px;font-weight:700;color:var(--white)}
.cta .btn{position:absolute;top:211px;height:37px;border-width:1px}
.cta-contact{left:487px;width:96px}
.cta-donate{left:589px;width:122px}

.strap{top:2567px;height:65px;background:var(--blue);display:flex;align-items:center;justify-content:center;color:var(--white);font-size:14px;font-weight:700}

/* footer */
.footer{top:2632px;height:146px;background:var(--footer-bg)}
.social{left:525px;top:34px;display:flex;gap:21px}
.social span{width:35px;height:35px;border:1px solid #666;border-radius:50%}
.copyright{left:0;right:0;top:96px;text-align:center;font-size:10px;color:#777}
.to-top{left:1166px;top:112px;width:20px;height:20px}
</style>
</head>
<body>

<header class="section hero">
  <div class="hero-photo" role="img" aria-label="Photo of a young child in a striped shirt against a dark blurred background"></div>
  <div class="abs logo">NORTHBEAM RESCUE FUND</div>
  <nav class="abs nav">
    <a href="#home">HOME</a>
    <a href="#about">ABOUT</a>
    <a href="#contact">CONTACT</a>
    <a href="#donate" class="nav-donate">DONATE</a>
  </nav>
  <h1 class="abs hero-title">Hello</h1>
  <p class="abs hero-tag">We Are A NGO – Northbeam Rescue Fund.</p>
  <a class="abs btn btn-fill hero-donate">Donate now</a>
  <a class="abs btn btn-line hero-more">Know more</a>
</header>

<section class="section about" id="about">
  <h2 class="section-title">About Us</h2>
  <div class="rule"></div>
  <p>Beacon Search Network is a non-profit corporation dedicated to the recovery of missing children and to the prevention of the abuse and endangerment of children. Beacon Search Network assists families searching for missing children by helping them to access local and federal law enforcement, advising them on the appropriate legal documents, and connecting them with other non-profit organizations or community resources that may help them in their search for their children.</p>
</section>
<div class="section about-band"><a class="btn">Know more</a></div>

<div class="section gallery">
  <div class="gallery-tile tile-1" role="img" aria-label="Photo of a child's hands"></div>
  <div class="gallery-tile tile-2" role="img" aria-label="Photo of a child sitting alone"></div>
  <div class="gallery-tile tile-3" role="img" aria-label="Photo of children outdoors"></div>
  <div class="gallery-tile tile-4" role="img" aria-label="Photo of a child in shadow"></div>
</div>

<section class="section donate-band" id="donate">
  <h2 class="section-title">Donate your car</h2>
  <div class="rule"></div>
</section>

<section class="section contact" id="contact">
  <h3 class="abs pitch-title">Help Find Missing Kids</h3>
  <ul class="abs pitch-list">
    <li>Fast Free Pickup – 24hr Response</li>
    <li>Tax Deduction – Easy To Do!</li>
    <li>No Emission Test Required</li>
  </ul>
  <form class="abs form">
    <label class="field-label">Your Name (required)</label>
    <div class="field"></div>
    <label class="field-label">Your Email (required)</label>
    <div class="field"></div>
    <label class="field-label">Subject</label>
    <div class="field"></div>
    <label class="field-label">Your Message</label>
    <div class="field field-area"></div>
    <span class="btn btn-fill send">Send</span>
  </form>
</section>

<section class="section stats">
  <div class="abs stat" style="left:130px">
    <div class="stat-num">800k</div>
    <div class="stat-label">Children are reported missing a year</div>
  </div>
  <div class="abs stat" style="left:450px">
    <div class="stat-num">750k</div>
    <div class="stat-label">Children have seen the Beacon Search<br>program</div>
  </div>
  <div class="abs stat" style="left:770px">
    <div class="stat-num">400+</div>
    <div class="stat-label">Open missing children cases</div>
  </div>
</section>

<section class="section cta" role="img" aria-label="Photo of a child walking at sunset among trees">
  <h2 class="cta-title">Help us Save those Children</h2>
  <a class="btn btn-line cta-contact">Contact</a>
  <a class="btn btn-line cta-donate">Donate</a>
</section>

<div class="section strap">Let’s take the next step and work together. We can save a life &amp; Unite a family.</div>

<footer class="section footer">
  <div class="abs social"><span></span><span></span><span></span></div>
  <p class="abs copyright">© 2018 Northbeam Rescue Fund. Give Wheels Forward 2018. All Rights Reserved / Designed and Developed by Kestrel Studio</p>
  <svg class="abs to-top" viewBox="0 0 20 20" aria-label="Back to top"><circle cx="10" cy="10" r="10" fill="#111"/><path d="M7 11.5 L10 8.5 L13 11.5" stroke="#ccc" stroke-width="1.5" fill="none"/></svg>
</footer>

</body>
</html>
```